Business Card Design

We are a manufacturing and distribution company with most of our customer base being supermarkets. We have established brand guidelines that are attached.

```html
<!DOCTYPE html>
<html lang="en">
<head>
<meta charset="UTF-8">
<title>Veltora Business Card</title>
<link href="https://fonts.googleapis.com/css2?family=Montserrat:wght@700;800&family=Open+Sans:wght@400;600&display=swap" rel="stylesheet">
<style>
  :root {
    --bg: #e6e7ea;
    --brand-red: #cf2a22;
    --brand-blue: #0a5fa3;
    --ink: #1d1d1f;
    --paper: #ffffff;
    --muted: #2a2a2c;
  }
  * { box-sizing: border-box; margin: 0; padding: 0; }
  html, body { width: 1200px; height: 1095px; overflow: hidden; }
  body {
    background: var(--bg);
    position: relative;
    font-family: "Open Sans", Arial, sans-serif;
  }
  .card {
    position: absolute;
    left: 250px;
    width: 700px;
    height: 400px;
    border-radius: 22px;
    overflow: hidden;
    box-shadow: 0 18px 40px rgba(0,0,0,0.18);
  }
  .card-front {
    top: 95px;
    background: linear-gradient(90deg, var(--brand-red) 0%, #8e4a57 38%, #5c5a7e 58%, var(--brand-blue) 100%);
    display: flex;
    align-items: center;
    justify-content: center;
  }
  .front-brand {
    display: flex;
    align-items: center;
    gap: 18px;
    color: var(--paper);
    font-family: "Montserrat", Arial, sans-serif;
    font-weight: 800;
    font-size: 58px;
    letter-spacing: 2px;
  }
  .brand-square {
    width: 40px;
    height: 40px;
    background: currentColor;
  }
  .card-back {
    top: 600px;
    background: var(--paper);
  }
  .back-brand {
    position: absolute;
    left: 60px;
    top: 170px;
    display: flex;
    align-items: center;
    gap: 14px;
    color: var(--ink);
    font-family: "Montserrat", Arial, sans-serif;
    font-weight: 800;
    font-size: 44px;
    letter-spacing: 1px;
  }
  .back-brand .brand-square { width: 30px; height: 30px; }
  .divider {
    position: absolute;
    left: 390px;
    top: 80px;
    width: 3px;
    height: 240px;
    display: flex;
    flex-direction: column;
  }
  .divider .seg-blue { flex: 1; background: var(--brand-blue); }
  .divider .seg-red { flex: 1.6; background: var(--brand-red); margin: 12px 0; }
  .details {
    position: absolute;
    left: 420px;
    top: 78px;
    color: var(--muted);
  }
  .person-name {
    font-family: "Montserrat", Arial, sans-serif;
    font-weight: 800;
    font-size: 27px;
    line-height: 1.1;
  }
  .first-name { color: var(--brand-red); }
  .last-name { color: var(--brand-blue); }
  .person-role { font-size: 15px; margin-top: 2px; }
  .address { font-size: 14px; line-height: 1.45; margin-top: 22px; }
  .contacts { list-style: none; margin-top: 14px; font-size: 14px; line-height: 1.6; }
  .contacts li { display: flex; align-items: center; gap: 8px; }
  .contacts svg { width: 12px; height: 12px; flex: none; }
</style>
</head>
<body>
  <section class="card card-front" aria-label="Card front">
    <div class="front-brand"><span class="brand-square"></span>VELTORA</div>
  </section>

  <section class="card card-back" aria-label="Card back">
    <div class="back-brand"><span class="brand-square"></span>VELTORA</div>

    <div class="divider"><span class="seg-blue"></span><span class="seg-red"></span><span class="seg-blue"></span></div>

    <div class="details">
      <h1 class="person-name"><span class="first-name">Dalen</span> <span class="last-name">Harwick</span></h1>
      <p class="person-role">Founder</p>
      <p class="address">48 Harbor Lane<br>Westfield, OR 97201</p>
      <ul class="contacts">
        <li>
          <svg viewBox="0 0 12 12" aria-hidden="true"><path d="M2.5 1 L4.5 1 L5.2 3.5 L4 4.5 Q5 7 7.5 8 L8.5 6.8 L11 7.5 L11 9.5 Q10.5 11 9 11 Q1 10 1 2.5 Q1 1 2.5 1Z" fill="var(--brand-red)"/></svg>
          +1 (555) 014 2290
        </li>
        <li>
          <svg viewBox="0 0 12 12" aria-hidden="true"><rect x="0.5" y="2" width="11" height="8" fill="var(--brand-red)"/><path d="M0.5 2 L6 6.5 L11.5 2" fill="none" stroke="#fff" stroke-width="1"/></svg>
          dh@veltora.com
        </li>
        <li>
          <svg viewBox="0 0 12 12" aria-hidden="true"><circle cx="6" cy="6" r="5" fill="none" stroke="var(--brand-red)" stroke-width="1.4"/><ellipse cx="6" cy="6" rx="2.2" ry="5" fill="none" stroke="var(--brand-red)" stroke-width="1"/><line x1="1" y1="6" x2="11" y2="6" stroke="var(--brand-red)" stroke-width="1"/></svg>
          www.veltora.com
        </li>
      </ul>
    </div>
  </section>
</body>
</html>
```